Property lawyer needs a website for new law firm Sydney

WHO AM I ?
I am a real estate development lawyer based in suburban Sydney Australia with over 14 years experience and have recently started my own law firm "Bramblewood Legal". The firm is just me (a female) at this stage. I need a website designed that is capable of being edited by me frequently (hoping this is easily done?!) and can be published with the domain name I own - www.bramblewoodlegal.com.au.
My areas of practice are:
* Property development (strata & community titling, due diligence, easements, by-laws and management statements, structuring etc)
* Conveyancing (sale and purchase of residential, commercial and retail property)
* General property law (caveats, transfers, related party transactions, easements, leases, powers of attorney etc).
WEBSITE REQUIREMENTS
I would like a website which conveys professionalism, has a fresh modern corporate look and is easy to navigate. The website will mostly be accessed by potential clients looking for information about me, my areas of practice and how to get in contact with me. My potential clients are corporate developers and individuals who are buying and selling property.
My logo for Bramblewood Legal (see attached) is simple, clean and professional looking. I would like the website to work with the logo without being too dark.
I haven't written all of the content yet, so please use filler text for everything and structure the menus as described above. The site will need to be capable of being updated and edited by me.
Other than that I will leave the design up to you.
Thanks and happy designing!
Target Market(s)
Professional developers and individuals buying and selling real estate
Industry/Entity Type
Real Estate
Coding
Coded - Design and coding required
Number of Pages Required
4 page
Requirements
Must have
- I would like a website which conveys professionalism, has a fresh modern corporate look and is easy to navigate. The website will mostly be accessed by potential clients looking for information about me, my areas of practice and how to get in contact with me. My potential clients are corporate developers and individuals who are buying and selling property.
- Please use my logo for Bramblewood Legal. I would like the website to work with the logo - the colours are a dark blue (C 100% M 50% B 50%) and grey (C10% B 40%). I don't want the website to be too dark though.
- I am thinking 4 pages. I would like links across the top of the page for "Practice Areas", "About us" and "Contact us" - these should lead to separate landing pages with the content to be inserted later.
- The contact page should contain space for a potential client to send an email enquiry to the following email address "enquiries@bramblewoodlegal.com.au". My contact details are set out in the attached letterhead (see attached).
- I would also like the home page to set out what my three Practice Areas are - Property Development; Conveyancing; General Property Law. Each area should have some filler text under it which will be completed later and a link to be able to take me to the "Practice Areas" page where more detail on each will be provided.
- Please select images that are relevant to my practice as a property lawyer. The photos you use will be the ones which I use so please choose wisely.
- I will need a link on the bottom of the home page showing that I am a member of "The Counsel Guild of NSW" (see attached logo).
- The bottom of each page should also include the following statement "Bramblewood Legal is a business name of Bramblewood Legal Pty Limited ACN 482 517 306, an incorporated legal practice regulated by the Legal Profession Act 2004. Liability limited by a scheme approved under the Professional Standards Legislation."
Nice to have
- Have attached an image of me (not the best) but at least its me. Consider whether to use on "About us" page
Should not have
- No images of gavels, scales of justice or law books.
- Images not to be too masculine
- Website not to be too dark

```html
<!DOCTYPE html>
<html lang="en">
<head>
<meta charset="utf-8">
<title>Bramblewood Legal — Property Law Services</title>
<link href="https://fonts.googleapis.com/css2?family=Bitter:wght@400;700&family=Cinzel:wght@700&family=Lato:wght@400;700&display=swap" rel="stylesheet">
<style>
:root{
  --navy:#0b3f6e;
  --navy-dark:#083257;
  --grey-logo:#9aa3ab;
  --ink:#2b2b2b;
  --text:#444;
  --panel:#ececec;
  --field-border:#d6d6d6;
  --bar:#909fab;
  --white:#fff;
}
*{box-sizing:border-box;margin:0;padding:0}
html,body{width:1010px;height:1200px;overflow:hidden;background:var(--white)}
body{position:relative;font-family:"Lato",sans-serif;color:var(--text)}

/* header */
.site-header{position:absolute;left:0;top:0;width:1010px;height:97px;border-top:1px solid var(--navy);background:var(--white)}
.brand{position:absolute;left:120px;top:32px;font-family:"Bitter",serif;font-weight:400;font-size:27px;letter-spacing:-0.5px;color:var(--navy);text-transform:uppercase}
.top-phone{position:absolute;left:544px;top:8px;display:flex;align-items:center;gap:6px;font-family:"Lato",sans-serif;font-weight:700;font-size:17px;color:var(--navy)}
.top-mail{position:absolute;left:690px;top:0;width:212px;height:30px;background:var(--navy);clip-path:polygon(0 0,100% 0,93% 100%,7% 100%);display:flex;align-items:center;justify-content:center;gap:7px;color:var(--white);font-size:13px}
.main-nav{position:absolute;top:56px;left:495px;display:flex;align-items:center;font-family:"Bitter",serif;font-size:13.5px;color:var(--ink);text-transform:uppercase}
.main-nav a{color:inherit;text-decoration:none;height:27px;line-height:27px;padding:0 15px}
.main-nav a.current{background:var(--navy);color:var(--white)}
.main-nav .practice{margin-left:7px;margin-right:20px}

/* hero */
.hero{position:absolute;left:0;top:97px;width:1010px;height:447px;
  background:linear-gradient(180deg,#8fb3d8 0%,#c9dbeb 35%,#9aa79a 55%,#6f9a45 80%,#8cbd3a 100%)}
.hero-title{position:absolute;left:0;top:152px;width:1010px;text-align:center;font-family:"Cinzel",serif;font-weight:700;font-size:39px;line-height:50px;color:var(--navy);text-shadow:0 0 14px rgba(255,255,255,.9),0 0 4px rgba(255,255,255,.8)}

/* practice areas */
.practice-band{position:absolute;left:0;top:544px;width:1010px;height:226px;background:var(--navy)}
.area{position:absolute;top:482px;width:230px;text-align:center;color:var(--white)}
.area-badge{width:146px;height:146px;margin:0 auto;border-radius:50%;background:var(--white);display:flex;align-items:center;justify-content:center;box-shadow:0 0 0 1px #ddd inset}
.area-badge .inner{width:132px;height:132px;border-radius:50%;border:2px solid #e3e3e3;display:flex;align-items:center;justify-content:center}
.area h2{font-family:"Bitter",serif;font-weight:400;font-size:18px;line-height:19px;margin-top:12px;height:38px;display:flex;align-items:flex-start;justify-content:center;text-transform:uppercase}
.area h2.single{padding-top:0}
.area p{font-size:11.5px;line-height:14px;margin-top:2px}
.area a{display:inline-block;margin-top:5px;font-size:11.5px;font-weight:700;color:var(--white)}

/* contact */
.contact{position:absolute;left:0;top:770px;width:1010px;height:276px;background:var(--panel)}
.section-title{font-family:"Bitter",serif;font-weight:700;font-size:17px;color:var(--ink);padding-bottom:6px;border-bottom:1px dotted #9a9a9a;display:flex;align-items:center;gap:10px}
.section-title span{color:var(--navy)}
.enquiry{position:absolute;left:108px;top:26px;width:537px}
.enquiry .lead{font-size:11.5px;color:var(--ink);margin:10px 0 0}
.form-grid{position:relative;margin-top:10px;height:160px}
.field{position:absolute;height:23px;background:var(--white);border:1px solid var(--field-border);border-radius:3px;font-size:9.5px;color:#333;padding:6px 9px}
.field.select::after{content:"";position:absolute;right:0;top:0;width:23px;height:21px;background:#eee;border-left:1px solid var(--field-border)}
.field.select svg{position:absolute;right:6px;top:7px;z-index:1}
.submit{position:absolute;left:467px;top:131px;width:69px;height:23px;background:linear-gradient(#1b5a95,var(--navy-dark));border-radius:2px;color:var(--white);font-weight:700;font-size:11px;text-align:center;line-height:23px}
.divider{position:absolute;left:677px;top:20px;width:1px;height:236px;background:#d4d4d4}
.info{position:absolute;left:706px;top:26px;width:196px}
.info ul{list-style:none;margin-top:14px;font-size:11px;line-height:14px;color:#555}
.info li{display:flex;gap:10px;margin-bottom:13px}
.info li svg{flex:none;margin-top:1px}

/* footer */
.legal{position:absolute;left:0;top:1046px;width:1010px;height:113px;background:var(--white)}
.legal p{position:absolute;left:121px;top:27px;width:580px;font-size:13.2px;line-height:19px;color:var(--ink)}
.membership{position:absolute;left:722px;top:22px;display:flex;align-items:center;gap:10px}
.membership .seal{width:56px;height:66px;background:#7a7a7a;border-radius:4px 4px 28px 28px}
.membership span{font-family:"Bitter",serif;font-size:12px;line-height:13px;color:#666;text-transform:uppercase;width:100px}
.bottom-bar{position:absolute;left:0;top:1159px;width:1010px;height:41px;background:var(--bar)}
.bottom-bar small{position:absolute;left:110px;top:13px;font-size:10.5px;color:var(--white)}
.social{position:absolute;left:797px;top:9px;display:flex;gap:5px}
.social span{width:22px;height:22px;border-radius:50%;background:var(--white)}
</style>
</head>
<body>

<header class="site-header">
  <div class="brand">Bramblewood Legal</div>
  <div class="top-phone">
    <svg width="20" height="20" viewBox="0 0 20 20"><circle cx="10" cy="10" r="9" fill="none" stroke="#333" stroke-width="1.4"/><path d="M7 5c1 0 1.5 2 1.2 2.6L7.5 8.5c.6 1.6 1.8 2.8 3.5 3.6l.9-.8c.6-.3 2.6.3 2.6 1.3 0 .9-1 1.7-2 1.6C9 14 6 11 5.5 7.7 5.4 6.4 6 5 7 5z" fill="#333"/></svg>
    02 9471 3260
  </div>
  <div class="top-mail">
    <svg width="14" height="10" viewBox="0 0 14 10"><rect width="14" height="10" fill="#fff"/><path d="M0 0l7 6 7-6" fill="none" stroke="#0b3f6e" stroke-width="1.3"/></svg>
    info@bramblewoodlegal.com.au
  </div>
  <nav class="main-nav">
    <a class="current" href="#">Home</a>
    <a class="practice" href="#">Practice Areas</a>
    <a href="#">About Us</a>
    <a href="#">Contact Us</a>
  </nav>
</header>

<section class="hero" role="img" aria-label="Photograph of a sunny suburban street with family houses, gardens, green lawns and blue sky">
</section>
<h1 class="hero-title">I Specialize In<br>Property&nbsp; Law Services</h1>

<section class="practice-band"></section>

<article class="area" style="left:103px">
  <div class="area-badge"><div class="inner">
    <svg width="80" height="70" viewBox="0 0 80 70"><path d="M40 6 62 24v18H18V24z" fill="#444"/><rect x="35" y="28" width="10" height="10" fill="#fff"/><path d="M6 46h14l14 6h18c4 0 4 6 0 6H36l12 2 20-8c4-2 7 3 3 5L48 68H20L6 62z" fill="#444"/></svg>
  </div></div>
  <h2>Property<br>Development</h2>
  <p>Lorem ipsum dolor sit amet, consectetuer adipiscing elit, sed diam nonummy nibh euismod tincidunt ut laoreet</p>
  <a href="#">Read More ››</a>
</article>

<article class="area" style="left:391px">
  <div class="area-badge"><div class="inner">
    <svg width="86" height="60" viewBox="0 0 86 60"><rect x="2" y="12" width="18" height="24" transform="rotate(-30 11 24)" fill="#444"/><rect x="66" y="12" width="18" height="24" transform="rotate(30 75 24)" fill="#444"/><path d="M18 30 34 16h16l18 14-18 20c-3 3-7 2-8-1-3 2-7 1-8-2-3 1-6 0-7-3-3 0-5-2-5-4z" fill="#444"/><path d="M44 18 34 28c2 3 6 3 8 0l6-6" fill="none" stroke="#fff" stroke-width="2"/></svg>
  </div></div>
  <h2>Conveyancing</h2>
  <p>Lorem ipsum dolor sit amet, consectetuer adipiscing elit, sed diam nonummy nibh euismod tincidunt ut laoreet</p>
  <a href="#">Read More ››</a>
</article>

<article class="area" style="left:679px">
  <div class="area-badge"><div class="inner">
    <svg width="70" height="66" viewBox="0 0 70 66"><path d="M35 2 68 18v5H2v-5z" fill="#444"/><rect x="7" y="26" width="9" height="28" fill="#444"/><rect x="22" y="26" width="9" height="28" fill="#444"/><rect x="39" y="26" width="9" height="28" fill="#444"/><rect x="54" y="26" width="9" height="28" fill="#444"/><rect x="2" y="56" width="66" height="8" fill="#444"/></svg>
  </div></div>
  <h2>General<br>Property Law</h2>
  <p>Lorem ipsum dolor sit amet, consectetuer adipiscing elit, sed diam nonummy nibh euismod tincidunt ut laoreet</p>
  <a href="#">Read More ››</a>
</article>

<section class="contact">
  <div class="enquiry">
    <h3 class="section-title">
      <svg width="20" height="14" viewBox="0 0 20 14"><rect width="20" height="14" fill="#333"/><path d="M0 0l10 8 10-8M0 14l7-7M20 14l-7-7" fill="none" stroke="#ececec" stroke-width="1.4"/></svg>
      Get In <span>Touch With Us</span>
    </h3>
    <p class="lead">Lorem ipsum dolor sit amet consectetuer adipiscing sed dmmy nibh</p>
    <div class="form-grid">
      <div class="field" style="left:0;top:0;width:261px">Name</div>
      <div class="field" style="left:278px;top:0;width:259px">Email</div>
      <div class="field" style="left:0;top:32px;width:261px">Phone Number</div>
      <div class="field select" style="left:278px;top:32px;width:259px">Enquiry Type
        <svg width="11" height="7" viewBox="0 0 11 7"><path d="M1 1l4.5 4.5L10 1" fill="none" stroke="#888" stroke-width="1.6"/></svg></div>
      <div class="field" style="left:0;top:63px;width:537px;height:55px">Your Message</div>
      <div class="submit">SUBMIT</div>
    </div>
  </div>
  <div class="divider"></div>
  <div class="info">
    <h3 class="section-title">Contact <span>Imformation</span></h3>
    <ul>
      <li><svg width="10" height="14" viewBox="0 0 10 14"><path d="M5 0a5 5 0 0 1 5 5c0 3-5 9-5 9S0 8 0 5a5 5 0 0 1 5-5z" fill="#0b3f6e"/><circle cx="5" cy="5" r="2" fill="#ececec"/></svg>
        <span>Lorem ipsum dolor sit consectetuer adipiscing elit, diam nonummy nibh Street No 5, zip Code: 897410</span></li>
      <li><svg width="12" height="12" viewBox="0 0 12 12"><path d="M2 0c1 0 2 2.5 1.6 3.2L2.8 4.3c.8 2 2.4 3.5 4.6 4.5l1-1C9 7.5 12 8.3 12 9.5c0 1.2-1.3 2.5-2.6 2.4C5 11.5.6 7.2.1 2.8 0 1.3.8 0 2 0z" fill="#0b3f6e"/></svg>
        <span>02 9471 3260</span></li>
      <li><svg width="12" height="9" viewBox="0 0 12 9"><rect width="12" height="9" fill="#0b3f6e"/><path d="M0 0l6 5 6-5" fill="none" stroke="#ececec" stroke-width="1"/></svg>
        <span>enquiries@bramblewoodlegal.com.au</span></li>
    </ul>
  </div>
</section>

<footer class="legal">
  <p>Bramblewood Legal is a business name of Bramblewood Legal Pty Limited ACN 482 517 306, an incorporated legal practice regulated by the Legal Profession Act 2004. Liability limited by a scheme approved under the Professional Standards Legislation</p>
  <div class="membership">
    <div class="seal" role="img" aria-label="Membership badge"></div>
    <span>Member of The Counsel Guild of NSW</span>
  </div>
</footer>

<div class="bottom-bar">
  <small>© 2015 BramblewoodLegal. All Rights Reserved</small>
  <div class="social" aria-label="Social links">
    <span></span><span></span><span></span><span></span>
  </div>
</div>

</body>
</html>
```